Corporate Web Design

Hello Designers,
Thank you for wanting to participate in designing a web design.
First off let me introduce ourselves, we are a precious metals refinery that is base in the west coast. Our Name is Harborline Precious Metals Refinery. Our sole goal for this website is simplicity yet cleanliness and elegance. We want to demonstrate the process and procedures of what we do and who we are.
The Lay out:
We want about 4-5 Tabs that will help guide our customers through our website with ease. Some ideas of what we want to call the tabs might be….
1. Home
- This tab will take them to the home page
2. Contact Us
- Our contact information
- Client contact form
- Some sort of membership form?
3. Pick-up Service
- This tab will explain how this process works and what it in tells.
- This page will also have a section for requirements.
- This pickup service will only be available for members and people that have a good account with us.
4. How it Works
- This page will explain who we are and how we work.
- I would like to somehow creatively show the process and the steps we take in melting their gold.
Effects:
An effect that I would want to see is a live precious metal stock price. This price will automatically update and post the most recent and current price on the market of what the gold, silver etc prices. Here is a link of a company that has something similar, http://kelvaro-refining.example/ what I like about this spot price pop up, is that it follows them all over the page. I like that idea.
I would also like some sort of slide show that has videos and demonstrations of our company and business.
These are all Websites of our competitors that we like many ideas from.
http://www.hlpmr.example/
What we like about this website is the tab that says “Request Pick-up” With a form that they have to fill out. We would want more than just a form; we would want some sort of membership application.
http://dovemetals.example/
What I like about this website is the slideshow. It’s very simple yet professional. This is something that I would like to incorporate into our website. I also like the live metal market price.
http://kelvaro-refining.example/
This is another example of a website that has a live spot price of the gold market. I like how the gold price follows you around the page. I would like to see some of your ideas with this.
http://www.quillmetals.example/
This website is very clean and simple. I like the colors. I would like a little more character than what they have but I like the simplicity.
The colors we like are black, white, silver, gold, Royal Blue etc; basically anything that creates a clean atmosphere. These colors match our logo and also have a very elegant and professional perception to them. Please do not limit yourselves to only our suggestions
These are links to our Logo with all different colors.
https://www.filecrate.example/s/a11b22c33d44e55/LOGO_black_background.png
https://www.filecrate.example/s/f66g77h88i99j00/LOGO_black.png
https://www.filecrate.example/s/k12l34m56n78o90/LOGO_transparent_background.png
https://www.filecrate.example/s/p21q43r65s87t09/LOGO_white_background.png
These are links to a brochure of our business that represents and shows the process of what we do and demonstrates who we are.
https://www.filecrate.example/s/u13v35w57x79y91/inside_1.pdf
https://www.filecrate.example/s/z24a46b68c80d02/inside_2.pdf
Bottom line we want to see examples of ideas and layouts that you have for a website. Please upload them and We will comment back on them.

```html
<!DOCTYPE html>
<html lang="en">
<head>
<meta charset="utf-8">
<title>Harborline</title>
<link href="https://fonts.googleapis.com/css2?family=Oswald:wght@600&family=Arimo:wght@400;700&display=swap" rel="stylesheet">
<style>
:root{
  --gold:#a8842a;
  --gold-dark:#7d611c;
  --ink:#262626;
  --charcoal:#2b2b2b;
  --band:#3a3a3a;
  --white:#ffffff;
  --text:#222222;
  --rule:#d9d9d9;
}
*{margin:0;padding:0;box-sizing:border-box}
html,body{width:969px;height:1200px;overflow:hidden;background:var(--white)}
body{position:relative;font-family:"Arimo",Arial,sans-serif;color:var(--text)}
.abs{position:absolute}
.topbar{left:0;top:0;width:969px;height:25px;background:linear-gradient(#b8933a,#8a6a22);color:var(--white);font-size:7px}
.topbar .info{position:absolute;top:8px;display:flex;align-items:center;gap:4px}
.social{position:absolute;top:5px;left:761px;display:flex;gap:3px}
.social span{width:14px;height:14px;border-radius:50%;background:#dfe8f2}
.header{left:0;top:25px;width:969px;height:76px;background:var(--charcoal)}
.wordmark{position:absolute;left:103px;top:24px;font-family:"Arimo",Arial,sans-serif;font-weight:700;font-size:26px;color:#e8e8e8;letter-spacing:.5px;white-space:nowrap}
.nav{position:absolute;left:412px;top:0;height:76px;display:flex;font-weight:700;font-size:9px;color:var(--white)}
.nav a{color:inherit;text-decoration:none;display:flex;align-items:center;padding:0 8px}
.nav a.active{background:#4a4a4a;color:#777;width:53px;justify-content:center;margin-right:13px}
.hero{left:0;top:101px;width:969px;height:427px;background:linear-gradient(180deg,#cfe0ee 0%,#8da596 25%,#6f8a78 60%,#5c7a4e 85%,#c0554a 100%)}
.hero-title{left:0;top:225px;width:296px;height:92px;background:rgba(40,40,40,.85);border-left:5px solid var(--gold)}
.hero-title h1{position:absolute;left:23px;top:16px;font-family:"Oswald",sans-serif;font-weight:600;font-size:27px;line-height:29px;color:var(--white);text-transform:uppercase;letter-spacing:-.3px}
.slide-btn{left:945px;width:24px;height:57px;background:var(--gold);display:flex;align-items:center;justify-content:center}
.pricebar{left:93px;top:534px;width:590px;height:51px;background:var(--charcoal);color:#ccc;font-size:10px}
.pricebar .lbl{position:absolute;top:8px}
.pricebar .val{position:absolute;top:27px;height:17px;background:var(--gold-dark);color:#e7d6a6;font-size:8px;line-height:17px;padding-left:4px}
.contact-btn{left:727px;top:534px;width:99px;height:51px;background:linear-gradient(#b08a2e,#8a6a22);color:var(--ink);font-weight:700;font-size:9px;display:flex;align-items:center;justify-content:center;letter-spacing:.3px}
.col h2{font-size:13px;font-weight:700;color:var(--ink);margin-bottom:8px;letter-spacing:.2px}
.col p{font-size:7.6px;line-height:10.7px;margin-bottom:10.7px;white-space:nowrap}
.more{display:inline-block;background:var(--gold-dark);color:#f0dfa8;font-size:7.5px;padding:5px 6px;margin-top:1px}
.vrule{width:1px;background:var(--rule)}
.video{left:491px;top:644px;width:335px;height:224px;background:var(--charcoal);border-radius:3px}
.video-frame{position:absolute;left:3px;top:3px;width:329px;height:201px;background:linear-gradient(135deg,#cfcfcf 0%,#9a9a9a 45%,#7a6a40 65%,#b8b8b8 100%)}
.play{position:absolute;left:142px;top:78px;width:38px;height:38px;border-radius:50%;background:rgba(120,90,20,.8)}
.footer-line{left:0;top:906px;width:969px;height:7px;background:var(--gold)}
.footer{left:0;top:913px;width:969px;height:248px;background:var(--charcoal);color:var(--white)}
.footer h3{position:absolute;top:33px;font-size:10.5px;font-weight:700;color:var(--gold)}
.fmenu{position:absolute;left:93px;top:61px;font-size:8px;list-style:none}
.fmenu li{height:23.7px}
.ftext{position:absolute;left:247px;top:57px;font-size:8.3px;line-height:12.2px;white-space:nowrap}
.post{position:absolute;left:449px;font-size:8.3px;line-height:12px;white-space:nowrap}
.post .date{color:var(--gold)}
.post-rule{position:absolute;left:446px;width:152px;height:1px;background:#4a4a4a}
.fdiv{position:absolute;top:33px;width:1px;height:175px;background:#444}
.field{position:absolute;background:var(--white)}
.flabel{position:absolute;font-size:7px;color:var(--white)}
.send{position:absolute;left:678px;top:197px;width:56px;height:15px;background:var(--gold-dark);color:#f0dfa8;font-size:7px;border-radius:2px;display:flex;align-items:center;justify-content:center}
.bottom{left:0;top:1161px;width:969px;height:39px;background:var(--band);color:var(--white)}
.bottom .wordmark-sm{position:absolute;left:138px;top:12px;font-family:"Arimo",Arial,sans-serif;font-weight:700;font-size:14px;color:#d8d8d8}
.bottom .copy{position:absolute;right:141px;top:8px;text-align:right;font-size:7.5px;line-height:13px}
</style>
</head>
<body>

<div class="abs topbar">
  <div class="info" style="left:411px">
    <svg width="7" height="9" viewBox="0 0 7 9"><path d="M3.5 0C1.6 0 0 1.5 0 3.4 0 6 3.5 9 3.5 9S7 6 7 3.4C7 1.5 5.4 0 3.5 0z" fill="#2b2b2b"/></svg>
    your address here your address here
  </div>
  <div class="info" style="left:551px">
    <svg width="9" height="9" viewBox="0 0 9 9"><path d="M2 0l2 2-1 1.5c.6 1.2 1.4 2 2.5 2.5L7 5l2 2-1.5 2C3.5 8.5.5 5.5 0 1.5z" fill="#2b2b2b"/></svg>
    123 456 7890 123
  </div>
  <div class="info" style="left:639px">
    <svg width="10" height="8" viewBox="0 0 10 8"><rect width="10" height="8" fill="#2b2b2b"/><path d="M0 0l5 4 5-4" stroke="#8a6a22" fill="none"/></svg>
    info@youremail.com
  </div>
  <div class="social"><span></span><span></span><span></span><span></span></div>
</div>

<header class="abs header">
  <div class="wordmark">Harborline</div>
  <nav class="nav">
    <a class="active" href="#">HOME</a>
    <a href="#">ABOUT US</a>
    <a href="#">PICK-UP SERVICES</a>
    <a href="#">HOW IT WORKS</a>
    <a href="#">REQUEST A PICK-UP</a>
  </nav>
</header>

<section class="abs hero" role="img" aria-label="Photo of the refinery's green two-storey building with staircase and flowering shrubs"></section>
<div class="abs hero-title"><h1>Harborline Precious<br>Metals Refineries</h1></div>
<div class="abs slide-btn" style="top:213px"><svg width="8" height="10" viewBox="0 0 8 10"><path d="M2 1l4 4-4 4" stroke="#fff" stroke-width="2" fill="none"/></svg></div>
<div class="abs slide-btn" style="top:273px"><svg width="8" height="10" viewBox="0 0 8 10"><path d="M6 1L2 5l4 4" stroke="#fff" stroke-width="2" fill="none"/></svg></div>

<div class="abs pricebar">
  <span class="lbl" style="left:10px">Real-time Price</span>
  <span class="lbl" style="left:118px">Last update</span>
  <span class="lbl" style="left:274px">Bid</span>
  <span class="lbl" style="left:325px">Ask</span>
  <span class="lbl" style="left:391px">Low</span>
  <span class="lbl" style="left:443px">High</span>
  <span class="lbl" style="left:510px">Change</span>
  <span class="val" style="left:11px;width:90px">Gold<span style="position:absolute;right:2px;top:3px;width:11px;height:11px;background:#e6e6e6"></span></span>
  <span class="val" style="left:118px;width:124px">Thu May 30, 5:48 AM CDT</span>
  <span class="val" style="left:274px;width:40px">1,400.61</span>
  <span class="val" style="left:325px;width:40px">1,401.11</span>
  <span class="val" style="left:391px;width:40px">1,389.12</span>
  <span class="val" style="left:443px;width:40px">1,410.86</span>
  <span class="val" style="left:510px;width:66px">+7.18 (0.52%)</span>
</div>
<svg class="abs" style="left:694px;top:549px" width="20" height="22" viewBox="0 0 20 22"><path d="M16 12a7 7 0 1 1-3-6" stroke="#555" stroke-width="3" fill="none"/><path d="M11 1l6 4-6 4z" fill="#555"/></svg>
<div class="abs contact-btn">CONTACT US</div>

<section class="abs col" style="left:93px;top:622px">
  <h2>WHO WE ARE?</h2>
  <p>Some text here Some text here Some text here<br>Some text here Some text here Some text here.</p>
  <p>Some text here Some text here Some text here<br>Some text here Some text here Some text here<br>Some text here Some text here Some text here<br>Some text here Some text here Some text here<br>Some text here Some text here Some text here<br>Some text here Some text here Some text here<br>Some text here Some text here Some text here<br>Some text here Some text here Some text here<br>Some text here Some text here Some text here<br>Some text here Some text here Some text here<br>Some text here Some text here Some text here</p>
  <p>Some text here Some text here Some text here<br>Some text here Some text here Some text here<br>Some text here.</p>
  <span class="more">Read More...</span>
</section>
<div class="abs vrule" style="left:276px;top:624px;height:249px"></div>
<section class="abs col" style="left:293px;top:622px">
  <h2>WHAT WE DO?</h2>
  <p>Some text here Some text here Some text here<br>Some text here Some text here Some text here.</p>
  <p>Some text here Some text here Some text here<br>Some text here Some text here Some text here<br>Some text here Some text here Some text here<br>Some text here Some text here Some text here<br>Some text here Some text here Some text here<br>Some text here Some text here Some text here<br>Some text here Some text here Some text here<br>Some text here Some text here Some text here<br>Some text here Some text here Some text here<br>Some text here Some text here Some text here<br>Some text here Some text here Some text here</p>
  <p>Some text here Some text here Some text here<br>Some text here Some text here Some text here<br>Some text here.</p>
  <span class="more">Read More...</span>
</section>
<div class="abs vrule" style="left:476px;top:624px;height:249px"></div>
<section class="abs col" style="left:491px;top:622px"><h2>LATEST VIDEOS</h2></section>
<div class="abs video">
  <div class="video-frame" role="img" aria-label="Video still of gloved hands scooping gold scrap into a container"></div>
  <div class="play"><svg style="position:absolute;left:14px;top:11px" width="12" height="16" viewBox="0 0 12 16"><path d="M0 0l12 8-12 8z" fill="#2b2b2b"/></svg></div>
  <svg style="position:absolute;left:6px;top:210px" width="320" height="10" viewBox="0 0 320 10">
    <path d="M0 1l7 4-7 4z" fill="#a8842a"/>
    <rect x="16" y="3" width="113" height="4" rx="2" fill="#e5e5e5"/>
    <circle cx="25" cy="5" r="4" fill="#a8842a"/>
    <rect x="268" y="4" width="2" height="3" fill="#ccc"/><rect x="272" y="3" width="2" height="4" fill="#ccc"/><rect x="276" y="2" width="2" height="5" fill="#ccc"/>
    <rect x="286" y="2" width="14" height="6" rx="2" fill="#eee"/>
    <rect x="306" y="1" width="8" height="8" fill="none" stroke="#ccc"/>
  </svg>
</div>

<div class="abs footer-line"></div>
<footer class="abs footer">
  <h3 style="left:93px">Menu</h3>
  <ul class="fmenu"><li>HOME</li><li>ABOUT US</li><li>PICK-UP SERVICES</li><li>HOW IT WORKS</li><li>REQUEST A PICK-UP</li><li>CONTACT US</li></ul>
  <div class="fdiv" style="left:208px"></div>
  <h3 style="left:247px">Some text here</h3>
  <div class="ftext">Some text here Some text here<br>Some text here Some text here<br>Some text here Some text here<br>Some text here Some text here<br>Some text here Some text here<br>Some text here Some text here<br>Some text here Some text here<br>Some text here Some text here<br>Some text here Some text here<br>Some text here Some text here<br>Some text here Some text here</div>
  <div class="fdiv" style="left:409px"></div>
  <h3 style="left:449px">Popular posts</h3>
  <div class="post" style="top:58px">Some text here Some text here<br>Some text here<br><span class="date">30/05/2013 - no comments</span></div>
  <div class="post-rule" style="top:106px"></div>
  <div class="post" style="top:116px">Some text here Some text here<br>Some text here<br><span class="date">30/05/2013 - no comments</span></div>
  <div class="post-rule" style="top:155px"></div>
  <div class="post" style="top:170px">Some text here Some text here<br>Some text here<br><span class="date">30/05/2013 - no comments</span></div>
  <div class="fdiv" style="left:637px"></div>
  <h3 style="left:678px">Contact us</h3>
  <div class="field" style="left:678px;top:57px;width:112px;height:13px"></div>
  <span class="flabel" style="left:797px;top:60px">Name*</span>
  <div class="field" style="left:678px;top:77px;width:112px;height:13px"></div>
  <span class="flabel" style="left:797px;top:80px">Email*</span>
  <div class="field" style="left:678px;top:98px;width:150px;height:83px"></div>
  <div class="send">Send Message</div>
  <span class="flabel" style="left:790px;top:201px">Clear form</span>
</footer>

<div class="abs bottom">
  <div class="wordmark-sm">Harborline</div>
  <div class="copy">Copyright 2013 &nbsp;www.harborlinepmr.example<br>All rights reserved. &nbsp;I &nbsp;Terms and Conditions &nbsp;I &nbsp;Privacy Policy</div>
</div>

</body>
</html>
```